POLITICAL CARD TO HAND OUT

A LITTLE LARGER THAN THE REGULAR BUSINESS CARD WITH THE ABOVE INFORMATION.

Industry/Entity Type

Business

Contact Information for Business Card

ELECT *DEAN MARLOW* FOR JUSTICE OF THE PEACE PCT 6-EXPERIENCED LEADERSHIP- WITH MY PICTURE ON IT- PHONE 281-555-3816-REPUBLICAN PRIMARY - EARLY VOTING FEB 18TH THRU FEB 28 AND ELECTION DAY IS MARCH 4TH, 2014- USE RED WHITE AND BLUE WITH SOME STARS.

Requirements
Must have
• A FIVE POINTED STAR ON EACH SIDE OF MY NAME

```html
<!DOCTYPE html>
<html lang="en">
<head>
<meta charset="utf-8">
<title>Elect Dean Marlow – Justice of the Peace</title>
<link rel="stylesheet" href="https://fonts.googleapis.com/css2?family=Bowlby+One&family=Open+Sans:wght@400;600;700;800&display=swap">
<style>
  :root {
    --red-bright: #d0232b;
    --red-deep: #8e1016;
    --white: #ffffff;
    --blue: #233f94;
    --blue-light: #4f78c4;
    --blue-star: #1f3a8f;
    --portrait-top: #8a2a25;
    --portrait-bottom: #1d1c22;
  }
  html, body {
    margin: 0;
    padding: 0;
    width: 1200px;
    height: 703px;
    overflow: hidden;
    background: var(--white);
  }
  .card {
    display: block;
    width: 1200px;
    height: 703px;
  }
  .elect-label {
    font-family: "Bowlby One", sans-serif;
    font-size: 46px;
    fill: var(--red-bright);
    stroke: var(--white);
    stroke-width: 3px;
    letter-spacing: 1px;
  }
  .candidate-name {
    font-family: "Bowlby One", sans-serif;
    font-size: 104px;
    fill: var(--white);
  }
  .office-title {
    font-family: "Open Sans", sans-serif;
    font-weight: 800;
    font-size: 70px;
    fill: var(--blue);
  }
  .slogan {
    font-family: "Open Sans", sans-serif;
    font-weight: 600;
    font-size: 45px;
    fill: var(--blue);
  }
  .race {
    font-family: "Open Sans", sans-serif;
    font-weight: 800;
    font-size: 60px;
    fill: var(--blue);
  }
  .phone {
    font-family: "Open Sans", sans-serif;
    font-weight: 600;
    font-size: 19px;
    fill: var(--white);
  }
  .date-heading {
    font-family: "Open Sans", sans-serif;
    font-weight: 700;
    font-size: 40px;
    fill: var(--white);
  }
  .date-line {
    font-family: "Open Sans", sans-serif;
    font-weight: 400;
    font-size: 27px;
    fill: var(--white);
  }
  .date-line.large { font-size: 31px; }
  .ordinal { font-size: 0.62em; }
  .star-white { fill: var(--white); }
  .star-red { fill: var(--red-bright); stroke: var(--white); stroke-width: 0.12; }
  .star-blue { fill: var(--blue-star); stroke: var(--white); stroke-width: 0.1; }
</style>
</head>
<body>
<svg class="card" viewBox="0 0 1200 703" xmlns="http://www.w3.org/2000/svg">
  <defs>
    <linearGradient id="red-field" x1="0" y1="0" x2="1" y2="0.3">
      <stop offset="0" stop-color="var(--red-bright)"/>
      <stop offset="1" stop-color="var(--red-deep)"/>
    </linearGradient>
    <linearGradient id="blue-field" x1="0" y1="1" x2="1" y2="0">
      <stop offset="0" stop-color="var(--blue-light)"/>
      <stop offset="0.6" stop-color="var(--blue)"/>
    </linearGradient>
    <linearGradient id="portrait-tone" x1="0" y1="0" x2="0" y2="1">
      <stop offset="0" stop-color="var(--portrait-top)"/>
      <stop offset="1" stop-color="var(--portrait-bottom)"/>
    </linearGradient>
    <symbol id="star" viewBox="-1.1 -1.1 2.2 2.2">
      <path d="M0,-1 L0.235,-0.324 L0.951,-0.309 L0.38,0.124 L0.588,0.809 L0,0.4 L-0.588,0.809 L-0.38,0.124 L-0.951,-0.309 L-0.235,-0.324 Z"/>
    </symbol>
  </defs>

  <!-- Flag bands -->
  <rect class="band-red" x="42" y="20" width="1138" height="663" fill="url(#red-field)"/>
  <path class="band-white" d="M42,372 C250,290 500,215 800,185 L1180,185 L1180,683 L42,683 Z" fill="var(--white)"/>
  <path class="band-blue" d="M42,683 L42,655 C200,590 450,470 770,395 L770,683 Z" fill="url(#blue-field)"/>

  <!-- Candidate portrait area -->
  <path class="portrait" d="M800,20 L1180,20 L1180,683 L760,683 L770,420 L800,330 Z" fill="url(#portrait-tone)" role="img" aria-label="Portrait photo of the candidate in a white cowboy hat, dark suit and tie"/>

  <!-- Stars beside the name -->
  <use href="#star" class="star-white" x="88" y="187" width="36" height="36"/>
  <use href="#star" class="star-white" x="682" y="93" width="36" height="36"/>

  <!-- Stars along the white band edge -->
  <use href="#star" class="star-red" x="55" y="293" width="50" height="50"/>
  <use href="#star" class="star-red" x="204" y="243" width="48" height="48"/>
  <use href="#star" class="star-red" x="343" y="209" width="48" height="48"/>
  <use href="#star" class="star-red" x="483" y="183" width="44" height="44"/>
  <use href="#star" class="star-red" x="623" y="177" width="42" height="42"/>
  <use href="#star" class="star-red" x="751" y="174" width="36" height="36"/>

  <!-- Stars along the blue edge -->
  <use href="#star" class="star-blue" x="68" y="621" width="52" height="52"/>
  <use href="#star" class="star-blue" x="204" y="556" width="48" height="48"/>
  <use href="#star" class="star-blue" x="335" y="498" width="46" height="46"/>
  <use href="#star" class="star-blue" x="465" y="456" width="42" height="42"/>
  <use href="#star" class="star-blue" x="587" y="422" width="38" height="38"/>
  <use href="#star" class="star-blue" x="700" y="400" width="34" height="34"/>

  <!-- Headline -->
  <text class="elect-label" x="42" y="83">Elect</text>
  <text class="candidate-name" x="132" y="235" textLength="560" lengthAdjust="spacingAndGlyphs" transform="rotate(-10 132 235)">Dean Marlow</text>

  <!-- Office and race -->
  <text class="office-title" x="75" y="400" textLength="726" lengthAdjust="spacingAndGlyphs" transform="rotate(-12.9 75 400)">Justice of the Peace</text>
  <text class="slogan" x="164" y="461" textLength="505" lengthAdjust="spacingAndGlyphs" transform="rotate(-16 164 461)">Experienced Leadership</text>
  <text class="race" x="78" y="578" textLength="754" lengthAdjust="spacingAndGlyphs" transform="rotate(-19 78 578)">Precinct 6  Republican Primary</text>

  <!-- Contact -->
  <text class="phone" x="722" y="464" text-anchor="end">(281)</text>
  <text class="phone" x="724" y="491" text-anchor="end">555-3816</text>

  <!-- Dates -->
  <text class="date-heading" x="702" y="547" text-anchor="end" textLength="250" lengthAdjust="spacingAndGlyphs">Early Voting</text>
  <text class="date-line" x="294" y="583" textLength="404" lengthAdjust="spacingAndGlyphs">February 18<tspan class="ordinal">th</tspan> - February 28<tspan class="ordinal">th</tspan></text>
  <text class="date-heading" x="261" y="628" textLength="278" lengthAdjust="spacingAndGlyphs">Election Day</text>
  <text class="date-line large" x="213" y="667" textLength="226" lengthAdjust="spacingAndGlyphs">March 4<tspan class="ordinal">th</tspan>, 2014</text>
</svg>
</body>
</html>
```